Kem7Dex Letterhead

Need a new letterhead for my law firm.
IDENTIFYING INFORMATION BELOW:
Ansel T Brightwater III
Attorney at Law
Address: 4832 Tillbury Rd, Ste 250, Dallas, TX 75204
Phone: 866-402-7183
Fax: 469-583-0271
Email: kem@kem7dex.example
Website: www.kem7dex.example

Colors
0054AA
0677BA
7BADD7
CADEEF
E8F1F8

Requirements
Must have
• Logo needs to be on the letterhead, along with identifying information which is included in the project description.

```html
<!DOCTYPE html>
<html lang="en">
<head>
<meta charset="utf-8">
<title>Kem7Dex Letterhead</title>
<link rel="stylesheet" href="https://fonts.googleapis.com/css2?family=Poppins:wght@300;400;600;700;800&display=swap">
<style>
  :root {
    --brand-blue: #0677BA;
    --brand-deep: #0054AA;
    --ink: #1c1c1e;
    --body-ink: #2a2a2a;
    --paper: #ffffff;
    --backdrop: #ffffff;
  }
  * { margin: 0; padding: 0; box-sizing: border-box; }
  html, body {
    width: 1200px; height: 2804px; overflow: hidden;
    background: var(--backdrop);
    font-family: "Poppins", sans-serif;
    color: var(--ink);
  }
  .letterhead {
    position: absolute; left: 50px; top: 626px;
    width: 1100px; height: 1552px;
    background: var(--paper);
    box-shadow: 0 6px 28px rgba(0,0,0,0.22);
    overflow: hidden;
  }
  .band { position: absolute; background: var(--brand-blue); }
  .band--top { right: 0; top: 0; width: 353px; height: 35px; border-bottom-left-radius: 35px; }
  .band--bottom { right: 0; bottom: 0; width: 342px; height: 33px; border-top-left-radius: 33px; }

  .brand {
    position: absolute; left: 73px; top: 62px;
    display: flex; align-items: center; gap: 16px;
  }
  .brand__mark { width: 22px; height: 22px; background: var(--brand-blue); }
  .brand__name {
    font-size: 58px; font-weight: 800; letter-spacing: 3px;
    color: var(--ink); line-height: 1;
  }

  .salutation {
    position: absolute; left: 80px; top: 226px;
    font-size: 26px; font-weight: 400;
  }
  .body-copy {
    position: absolute; left: 73px; top: 282px; width: 934px;
    font-size: 16.4px; line-height: 22.2px; font-weight: 400;
    color: var(--body-ink); text-align: justify;
  }
  .body-copy p + p { margin-top: 22px; }

  .signature {
    position: absolute; left: 73px; top: 1146px;
  }
  .signature__line {
    width: 406px; margin-left: 10px;
    border-top: 2px dashed var(--ink);
  }
  .signature__name { margin-top: 22px; font-size: 29px; font-weight: 700; letter-spacing: -0.5px; }
  .signature__title { font-size: 27px; font-weight: 300; margin-top: 2px; }

  .contact-list {
    position: absolute; left: 88px; top: 1340px;
    list-style: none;
  }
  .contact-list li {
    display: flex; align-items: center; gap: 18px;
    height: 29px; font-size: 21px; font-weight: 400;
  }
  .contact-list li.is-number { font-weight: 600; }
  .contact-list svg { width: 22px; height: 22px; flex: none; fill: none; stroke: var(--brand-blue); stroke-width: 2; }
  .contact-list svg .solid { fill: var(--brand-blue); stroke: none; }
</style>
</head>
<body>
<main class="letterhead">
  <div class="band band--top"></div>
  <div class="band band--bottom"></div>

  <header class="brand">
    <span class="brand__name">KEM7DEX</span>
    <span class="brand__mark"></span>
  </header>

  <p class="salutation">Dear Sir,</p>

  <section class="body-copy">
    <p>Quis ipsum suspendisse ultrices gravida. Risus commodo viverra maecenas accumsan lacus vel facilisis. Lorem ipsum dolor sit amet, consectetur adipiscing elit, sed do eiusmod tempor incididunt ut labore et dolore magna aliqua. Quis ipsum suspendisse ultrices gravida. Risus commodo viverra maecenas accumsan lacus vel facilisis. Lorem ipsum dolor sit amet, consectetur adipiscing elit, sed do eiusmod tempor incididunt ut labore et dolore magna aliqua. Quis ipsum suspendisse ultrices gravida. Risus commodo viverra maecenas accumsan lacus vel facilisis. Lorem ipsum dolor sit amet, consectetur adipiscing elit, sed do eiusmod tempor incididunt ut labore et dolore magna aliqua. Quis ipsum suspendisse ultrices gravida. Risus commodo viverra maecenas accumsan lacus vel facilisis.</p>
    <p>Lorem ipsum dolor sit amet, consectetur adipiscing elit, sed do eiusmod tempor incididunt ut labore et dolore magna aliqua. Quis ipsum suspendisse ultrices gravida. Risus commodo viverra maecenas accumsan lacus vel facilisis. Lorem ipsum dolor sit amet, consectetur adipiscing elit, sed do eiusmod tempor incididunt ut labore et dolore magna aliqua. Quis ipsum suspendisse ultrices gravida. Risus commodo viverra maecenas accumsan lacus vel facilisis. Lorem ipsum dolor sit amet, consectetur adipiscing elit, sed do eiusmod tempor incididunt ut labore et dolore magna aliqua. Quis ipsum suspendisse ultrices gravida. Risus commodo viverra maecenas accumsan lacus vel facilisis. Lorem ipsum dolor sit amet, consectetur adipiscing elit, sed do eiusmod tempor incididunt ut labore et dolore magna aliqua. Quis ipsum suspendisse ultrices gravida. Risus commodo viverra maecenas accumsan lacus vel facilisis.</p>
    <p>Lorem ipsum dolor sit amet, consectetur adipiscing elit, sed do eiusmod tempor incididunt ut labore et dolore magna aliqua. Quis ipsum suspendisse ultrices gravida. Risus commodo viverra maecenas accumsan lacus vel facilisis. Lorem ipsum dolor sit amet, consectetur adipiscing elit, sed do eiusmod tempor incididunt ut labore et dolore magna aliqua. Quis ipsum suspendisse ultrices gravida. Risus commodo viverra maecenas accumsan lacus vel facilisis. Lorem ipsum dolor sit amet, consectetur adipiscing elit, sed do eiusmod tempor incididunt ut labore et dolore magna aliqua. Quis ipsum suspendisse ultrices gravida. Risus commodo viverra maecenas accumsan lacus vel facilisis. Lorem ipsum dolor sit amet, consectetur adipiscing elit, sed do eiusmod tempor incididunt ut labore et dolore magna aliqua. Quis ipsum suspendisse ultrices gravida. Risus commodo viverra maecenas accumsan lacus vel facilisis. Lorem ipsum dolor sit amet, consectetur adipiscing elit, sed do eiusmod tempor incididunt ut labore et dolore magna aliqua. Quis ipsum suspendisse ultrices gravida. Risus commodo viverra maecenas accumsan lacus vel facilisis. Lorem ipsum dolor sit amet, consectetur adipiscing elit, sed do eiusmod tempor incididunt ut labore et dolore magna aliqua. Quis ipsum suspendisse ultrices gravida. Risus commodo viverra maecenas accumsan lacus vel facilisis.</p>
  </section>

  <section class="signature">
    <div class="signature__line"></div>
    <p class="signature__name">Ansel T Brightwater III</p>
    <p class="signature__title">Attorney at Law</p>
  </section>

  <ul class="contact-list">
    <li class="is-number">
      <svg viewBox="0 0 24 24"><path d="M5 3l4 1 1 5-2.5 1.5a12 12 0 0 0 6 6L15 14l5 1 1 4-2 2C10 21 3 14 3 5z"/></svg>
      866-402-7183
    </li>
    <li class="is-number">
      <svg viewBox="0 0 24 24"><rect x="7" y="3" width="10" height="6"/><rect class="solid" x="3" y="9" width="18" height="9" rx="2"/><rect x="7" y="14" width="10" height="7" fill="#fff"/></svg>
      469-583-0271
    </li>
    <li>
      <svg viewBox="0 0 24 24"><rect x="3" y="6" width="18" height="13" rx="1"/><path d="M3 7l9 7 9-7"/></svg>
      kem@kem7dex.example
    </li>
    <li>
      <svg viewBox="0 0 24 24"><circle cx="12" cy="12" r="9"/><ellipse cx="12" cy="12" rx="4" ry="9"/><path d="M3 12h18M5 7h14M5 17h14"/></svg>
      www.kem7dex.example
    </li>
    <li>
      <svg viewBox="0 0 24 24"><path d="M12 21s-6-6.5-6-11a6 6 0 0 1 12 0c0 4.5-6 11-6 11z"/><circle cx="12" cy="10" r="2.2"/><path d="M5 21h14"/></svg>
      4832 Tillbury Rd, Ste 250, Dallas, TX 75204
    </li>
  </ul>
</main>
</body>
</html>
```